Vodka Bottle Label - Lune Vodka

I need a bottle label for a vodka I'd like to make called Lune Vodka.
I would like a label that looks elegant and fresh. I would like some mountains and colours to be red and white. Open to other colours being added but not too colourful. "Lune" means fresh, dawn in polish, i would like if mountains or something extra was added to the label too. I would like the Lune Vodka name not to be too small.
The vodka is made in australia and is 37%.

I would love to have a little bit of gold colour in the label!

I will provide the back label words when completing my decision.

i'd like to make it more simple and less european looking. More australian.

I saw a bottle like this and i did like the concept.

https://www.oakbarrelcellars.com.au/spirits/grey-vodka-range?srsltid=XqTz81mwkPLd04-hr-q7w93nfbzkgd_mR2yTpaMWxJeQ6vcbTnZsLpo

Target Market(s)

Vodka Drinkers

Industry/Entity Type

Alcohol

Colors
EB3D1F
EC4F4E
F09395
F8D3D4
FCEDEE

Requirements
Must have
• red and white colours incorporated, mountains or freshness on it.
Nice to have
• Fresh and clean look. Classy

```html
<!DOCTYPE html>
<html lang="en">
<head>
<meta charset="utf-8">
<title>Lune Vodka – Front Label</title>
<link rel="stylesheet" href="https://fonts.googleapis.com/css2?family=Abril+Fatface&family=Montserrat:wght@500;700&family=Oswald:wght@400;500&display=swap">
<style>
  :root {
    --paper: #ffffff;
    --canvas: #f6f6f6;
    --label-red: #d0323c;
    --band-red-light: #cf343e;
    --band-red-dark: #8c3d44;
    --slate: #3e5157;
    --hairline: #8a8a8a;
    --white: #ffffff;
  }
  * { margin: 0; padding: 0; box-sizing: border-box; }
  html, body { width: 900px; height: 1200px; overflow: hidden; background: var(--canvas); }
  .canvas { position: relative; width: 900px; height: 1200px; }
  .label-art { position: absolute; inset: 0; }
  .brand-mark {
    position: absolute; left: 50%; top: 112px; transform: translateX(-50%);
    background: var(--canvas); padding: 4px 18px;
    font-family: "Montserrat", sans-serif; font-weight: 700; font-size: 46px;
    letter-spacing: 6px; color: var(--slate); line-height: 1;
  }
  .product-name {
    position: absolute; left: 0; right: 0; top: 590px; text-align: center;
    font-family: "Abril Fatface", serif; font-size: 178px; line-height: 1;
    color: var(--label-red); letter-spacing: 2px;
    transform: scaleX(0.86);
  }
  .product-type {
    position: absolute; left: 0; right: 0; top: 800px; text-align: center;
    font-family: "Montserrat", sans-serif; font-weight: 500; font-size: 80px;
    line-height: 1; letter-spacing: 12px; color: var(--slate); padding-left: 12px;
  }
  .edition {
    position: absolute; left: 0; right: 0; top: 940px; text-align: center; color: var(--white);
    font-family: "Oswald", sans-serif;
  }
  .edition-title {
    display: inline-flex; align-items: center; gap: 12px;
    font-size: 40px; font-weight: 500; line-height: 1; letter-spacing: 1px;
  }
  .edition-title::before, .edition-title::after {
    content: ""; width: 62px; height: 8px;
    border-top: 1.5px solid var(--white); border-bottom: 1.5px solid var(--white);
  }
  .edition-sub { font-size: 18px; letter-spacing: 1px; margin-top: 6px; }
  .spec-pill {
    position: absolute; left: 214px; top: 1024px; width: 464px; height: 56px;
    border: 1.5px solid var(--white); border-radius: 28px;
    display: flex; align-items: center; justify-content: space-around;
    color: var(--white); font-family: "Oswald", sans-serif;
  }
  .spec { font-size: 26px; letter-spacing: 1px; }
  .spec-origin { font-size: 14px; line-height: 1.1; text-align: center; font-weight: 500; }
  .spec-divider { width: 1.5px; height: 34px; background: var(--white); }
  .grain-note {
    position: absolute; left: 0; right: 0; top: 1090px; text-align: center;
    font-family: "Oswald", sans-serif; font-size: 20px; color: var(--white); letter-spacing: 0.5px;
  }
</style>
</head>
<body>
<main class="canvas">
  <svg class="label-art" width="900" height="1200" viewBox="0 0 900 1200" aria-hidden="false">
    <defs>
      <linearGradient id="bandGradient" x1="0" y1="0" x2="1" y2="1">
        <stop offset="0" stop-color="var(--band-red-light)"/>
        <stop offset="0.55" stop-color="var(--band-red-dark)"/>
        <stop offset="1" stop-color="var(--band-red-light)"/>
      </linearGradient>
      <linearGradient id="sceneGradient" x1="0" y1="0" x2="0" y2="1">
        <stop offset="0" stop-color="#dfe3e4" stop-opacity="0"/>
        <stop offset="0.35" stop-color="#b9c4c7"/>
        <stop offset="0.7" stop-color="#3b4a4c"/>
        <stop offset="1" stop-color="#b8652e"/>
      </linearGradient>
      <clipPath id="labelClip">
        <path d="M189,1100 L189,245 Q189,195 240,190 L450,150 L660,190 Q711,195 711,245 L711,1100 Q711,1154 657,1154 L243,1154 Q189,1154 189,1100 Z"/>
      </clipPath>
      <path id="arcText" d="M325,470 A125,125 0 0 1 575,470"/>
    </defs>

    <path class="label-body" d="M189,1100 L189,245 Q189,195 240,190 L450,150 L660,190 Q711,195 711,245 L711,1100 Q711,1154 657,1154 L243,1154 Q189,1154 189,1100 Z"
          fill="var(--paper)" stroke="var(--label-red)" stroke-width="5"/>
    <path class="label-inner-line" d="M200,903 L200,250 Q200,205 245,201 L450,163 L655,201 Q700,205 700,250 L700,903"
          fill="none" stroke="var(--hairline)" stroke-width="1.2"/>

    <rect class="label-band" x="189" y="903" width="522" height="260" fill="url(#bandGradient)" clip-path="url(#labelClip)"/>

    <path class="badge-arch" d="M293,470 A157,160 0 0 1 607,470 L568,470 A118,118 0 0 0 332,470 Z" fill="var(--slate)"/>
    <text font-family="Oswald, sans-serif" font-size="19" fill="var(--white)" letter-spacing="1">
      <textPath href="#arcText" startOffset="50%" text-anchor="middle">AUSTRALIAN VODKA</textPath>
    </textPath></text>

    <rect class="mountain-scene" x="250" y="385" width="400" height="195" rx="6"
          fill="url(#sceneGradient)" role="img" aria-label="Illustration of a snowy mountain peak behind a pine forest with autumn foliage"/>
  </svg>

  <div class="brand-mark">LUNE</div>
  <h1 class="product-name">LUNE</h1>
  <div class="product-type">VODKA</div>

  <div class="edition">
    <div class="edition-title">ORIGINAL</div>
    <div class="edition-sub">LIMITED EDITION</div>
  </div>

  <div class="spec-pill">
    <span class="spec">37% VOL</span>
    <span class="spec-divider"></span>
    <span class="spec-origin">MADE IN<br>AUSTRALIA</span>
    <span class="spec-divider"></span>
    <span class="spec">750 ML</span>
  </div>

  <div class="grain-note">100% PURE GRAIN</div>
</main>
</body>
</html>
```